Tin Lantern
Business Cards and Letterhead
Tin Lantern -
Creative Brief
Professional
Gareth Pulvey
Practice Manager
48 Mill Lane Egham Surrey KT17 4RD
gareth@tin-lantern.co.uk
www.tin-lantern.co.uk
We are an Accountancy firm; so for the letterhead we will require another logo to be incorporated (maybe at the bottom) this logo is our governing body.
We have not given the back of the card much thought, so all ideas are welcome.

```html
<!DOCTYPE html>
<html lang="en">
<head>
<meta charset="utf-8">
<title>Tin Lantern – Business Card</title>
<link rel="stylesheet" href="https://fonts.googleapis.com/css2?family=Source+Sans+3:wght@400;600&display=swap">
<style>
  :root {
    --backdrop: #2b1f12;
    --card-white: #ffffff;
    --card-grey: #a6a7aa;
    --band-grey: #b3b4b6;
    --accent-orange: #f7941d;
    --text-grey: #5c5d60;
    --text-dark: #3a3b3d;
  }
  * { margin: 0; padding: 0; box-sizing: border-box; }
  html, body {
    width: 1200px; height: 901px; overflow: hidden;
    background: var(--backdrop);
    font-family: "Source Sans 3", sans-serif;
  }
  .card {
    position: absolute; left: 302px;
    width: 638px;
    overflow: hidden;
  }
  .card-front { top: 73px; height: 370px; background: var(--card-white); }
  .card-back  { top: 475px; height: 360px; background: var(--card-grey); }

  .brand {
    position: absolute; display: flex; align-items: center; gap: 12px;
    font-weight: 600; line-height: 1; white-space: nowrap;
  }
  .brand-mark { display: block; flex: none; }
  .card-front .brand { left: 29px; top: 58px; font-size: 46px; color: var(--accent-orange); }
  .card-front .brand-mark { width: 34px; height: 34px; background: var(--accent-orange); }

  .holder { position: absolute; left: 338px; top: 190px; }
  .holder-name { font-size: 25px; font-weight: 600; color: var(--accent-orange); line-height: 1.1; }
  .holder-role { font-size: 19px; color: var(--text-grey); line-height: 1.1; }

  .contact {
    position: absolute; left: 338px; top: 256px;
    font-size: 18px; line-height: 19.5px; color: var(--text-dark);
    display: grid; grid-template-columns: 64px auto; column-gap: 0;
    white-space: nowrap;
  }
  .contact dt { font-weight: 400; }
  .contact .email-row { grid-column: 1 / 3; }

  .address {
    position: absolute; left: 31px; top: 266px;
    font-size: 18px; line-height: 21px; color: var(--text-dark); font-style: normal;
    white-space: nowrap;
  }
  .address .web { color: var(--accent-orange); }

  .band-grey { position: absolute; left: 27px; right: 0; top: 341px; height: 14px; background: var(--band-grey); }
  .band-orange { position: absolute; left: 0; right: 0; top: 355px; height: 9px; background: var(--accent-orange); }

  .stripe-white { position: absolute; left: 0; top: 0; bottom: 0; width: 17px; background: var(--card-white); }
  .stripe-orange { position: absolute; left: 17px; top: 0; bottom: 0; width: 14px; background: var(--accent-orange); }

  .card-back .brand { left: 31px; right: 0; justify-content: center; top: 138px; font-size: 56px; color: var(--card-white); }
  .card-back .brand-mark { width: 40px; height: 40px; background: var(--card-white); }
  .back-web {
    position: absolute; left: 175px; top: 255px;
    font-size: 18px; letter-spacing: 4px; color: var(--card-white);
    white-space: nowrap;
  }
</style>
</head>
<body>
  <section class="card card-front">
    <div class="brand"><span class="brand-mark"></span><span class="brand-name">TinLantern</span></div>

    <div class="holder">
      <p class="holder-name">Gareth Pulvey</p>
      <p class="holder-role">Practice Manager</p>
    </div>

    <dl class="contact">
      <div class="email-row">E-mail: gareth@tin-lantern.co.uk</div>
      <dt>Cell:</dt><dd>07700 900417</dd>
      <dt>Phone:</dt><dd>01632 960582</dd>
      <dt>Fax:</dt><dd>01632 960739</dd>
    </dl>

    <address class="address">
      48 Mill Lane, Ashcombe<br>
      Dunmore, KT17 4RD<br>
      <span class="web">www.tin-lantern.co.uk</span>
    </address>

    <div class="band-grey"></div>
    <div class="band-orange"></div>
  </section>

  <section class="card card-back">
    <div class="stripe-white"></div>
    <div class="stripe-orange"></div>
    <div class="brand"><span class="brand-mark"></span><span class="brand-name">TinLantern</span></div>
    <p class="back-web">www.tin-lantern.co.uk</p>
  </section>
</body>
</html>
```